Ridgeline Outfitters Business Cards

Recently had a logo done with Artflockr and now looking for a business card to go along with it.

Target Market(s)

Ridgeline Outfitters is a weapons dealer. My market will be primarily men, hunting, shooting type.

Industry/Entity Type

Business

Contact Information for Business Card

I selected double sided, but this is not required, single or double is going to be fine. I picture the logo on one side, or perhaps just the circle which contains "RO" with the remaining info on the other side.

Font styles to use
Sans Serif

Requirements
Must have
• My name: Wesley Holm
• Title: Owner
• tel: 612-555-0378
• web: www.ridgelineoutfittersmn.example
Nice to have
• I like the concept of a black business card. I would like to keep the colors monotone, black, grey, white or red. Red is acceptable because it is in the logo. I have also seen cards that are matte black with shiny black as well, perhaps for the logo (or circle RO) part of the logo.
• I will upload a couple of the logos for use, and also an example I just found of the black on black. and some others that have a nice contrast.
Should not have
• lots of colors are not wanted.

```html
<!DOCTYPE html>
<html lang="en">
<head>
<meta charset="utf-8">
<title>Ridgeline Outfitters – Business Cards</title>
<link rel="stylesheet" href="https://fonts.googleapis.com/css2?family=Open+Sans:wght@400;600;700&display=swap">
<style>
  :root {
    --backdrop: #3a3d42;
    --card: #1b1b1c;
    --card-edge: #2a2a2b;
    --gloss-black: #0a0a0a;
    --mark-grey: #8d8f92;
    --brand-red: #e0161f;
    --name-grey: #9a9a9a;
    --text-light: #cfcfcf;
    --rule: #4a4a4c;
  }
  * { margin: 0; padding: 0; box-sizing: border-box; }
  html, body {
    width: 1200px; height: 864px; overflow: hidden;
    background: var(--backdrop);
    font-family: "Open Sans", Arial, sans-serif;
  }
  .sheet {
    width: 1200px; height: 864px;
    display: flex; flex-direction: column; align-items: center; justify-content: center;
    gap: 40px;
  }
  .card {
    position: relative;
    width: 560px; height: 320px;
    background: var(--card);
    border: 1px solid var(--card-edge);
    box-shadow: 0 10px 30px rgba(0,0,0,.45);
  }

  /* Back of card */
  .card-back .mark {
    position: absolute; left: 50%; top: 46px; transform: translateX(-50%);
    display: flex; align-items: center; gap: 16px;
  }
  .card-back .mark-circle {
    width: 150px; height: 150px; border-radius: 50%;
    border: 10px solid var(--gloss-black);
  }
  .card-back .mark-name {
    font-weight: 700; font-size: 22px; letter-spacing: 1px;
    color: var(--gloss-black); text-transform: uppercase; white-space: nowrap;
  }
  .card-back .web {
    position: absolute; left: 0; right: 0; bottom: 44px;
    text-align: center; font-size: 15px; color: var(--brand-red);
  }

  /* Front of card */
  .card-front .brand {
    position: absolute; top: 36px; right: 40px;
    display: flex; align-items: center; gap: 14px;
  }
  .card-front .brand-circle {
    width: 66px; height: 66px; border-radius: 50%;
    border: 5px solid var(--mark-grey);
  }
  .card-front .brand-name {
    font-weight: 700; font-size: 22px; letter-spacing: 1px;
    color: var(--brand-red); text-transform: uppercase;
  }
  .card-front .person {
    position: absolute; left: 62px; top: 120px;
  }
  .card-front .person-name {
    font-weight: 700; font-size: 20px; color: var(--name-grey);
  }
  .card-front .person-title {
    font-size: 14px; color: var(--name-grey);
  }
  .card-front .divider {
    position: absolute; left: 0; right: 40px; top: 182px;
    height: 1px; background: var(--rule);
  }
  .card-front .contact {
    position: absolute; right: 40px; top: 246px;
    list-style: none; text-align: right;
  }
  .card-front .contact li {
    display: flex; align-items: center; justify-content: flex-end; gap: 10px;
    font-size: 15px; color: var(--text-light); line-height: 24px;
  }
  .card-front .contact svg { width: 12px; height: 12px; fill: var(--name-grey); }
</style>
</head>
<body>
<main class="sheet">
  <section class="card card-back" aria-label="Card back">
    <div class="mark">
      <span class="mark-circle"></span>
      <span class="mark-name">Ridgeline Outfitters</span>
    </div>
    <p class="web">www.ridgelineoutfittersmn.example</p>
  </section>

  <section class="card card-front" aria-label="Card front">
    <div class="brand">
      <span class="brand-circle"></span>
      <span class="brand-name">Ridgeline Outfitters</span>
    </div>
    <div class="person">
      <p class="person-name">Wesley Holm</p>
      <p class="person-title">Owner</p>
    </div>
    <div class="divider"></div>
    <ul class="contact">
      <li>612-555-0378
        <svg viewBox="0 0 24 24" aria-hidden="true"><path d="M6.6 10.8a15.1 15.1 0 0 0 6.6 6.6l2.2-2.2a1 1 0 0 1 1-.25 11.4 11.4 0 0 0 3.6.57 1 1 0 0 1 1 1V20a1 1 0 0 1-1 1A17 17 0 0 1 3 4a1 1 0 0 1 1-1h3.5a1 1 0 0 1 1 1c0 1.25.2 2.45.57 3.57a1 1 0 0 1-.25 1z"/></svg>
      </li>
      <li>info@ridgelineoutfittersmn.example
        <svg viewBox="0 0 24 24" aria-hidden="true"><path d="M2 5h20v14H2z M4 7v.5l8 5 8-5V7z" fill-rule="evenodd"/></svg>
      </li>
    </ul>
  </section>
</main>
</body>
</html>
```